We are a printed circuit board manufacturer. Need a company professional web site to allow our potential customers to know more about our background, capability and our products. The web site will contain three languages, which are Chinese, English and Japanese. Our audience are mainly electronic companies that procure printed circuit boards. I have a word document that have all the required text in all three languages. The final design should communicate the impression that we embrace quality, trustworthiness and long term partnership business principles.
We should have sections that allow us to post pictures of our facilities.
I have added the three files in three different languages.
Some of the information is below:
Background
RVD Worldwide Limited (RVD) was set up in Hong Kong in 2007 by two Hong Kong entrepreneurs, Mr. Lok Fai Tam and Mr. Wai Ho. We acquired the single sided printed circuit board factory located in Dongguan City, Guangdong Province, China, from Valtor Corporation of the U.S. in 2007. In addition to RVD, Mr. Tam and Mr. Ho also own Brightrail Systems Company Limited, a semiconductor company based in Hong Kong since 1997 with a total investment of over US$100 million. Brightrail is engaged in the manufacturing of flexible substrates and MEMS assembly business.
RVD has been awarded TS 16949 and ISO14000 certificates since 2009 and 2004 respectively.
Business Principles
RVD Worldwide Limited strives to be a professional top notched printed circuit board supplier. We embrace four “EXCELLENCE” principles, namely, excellence in quality, excellence in prices, excellence in services and excellence in on time delivery.
We approach each customer with a long-term partnership view that delivers the lowest ownership costs and highest total values to our customers. We customize quotations and solutions in order to allow our customers to win more businesses. We believe by thinking from our customers’ points of view we will be able to create a WIN-WIN relationship.
Customers
Due to our excellent quality, services and production systems, RVD Worldwide Limited manage to service a number of large Japanese and US customers, which include:
Technical capability overview
Below is an overview of our current capability:
Target Market(s)
Electronic companies buyers
Industry/Entity Type
Business
Requirements
Must have
- Capability description
Should not have
- no cartoon

```html
<!DOCTYPE html>
<html lang="en">
<head>
<meta charset="utf-8">
<title>RVD Worldwide Limited</title>
<link rel="stylesheet" href="https://fonts.googleapis.com/css2?family=Questrial&family=Arimo:wght@400;700&display=swap">
<style>
  :root {
    --page-blue: #6097d6;
    --page-blue-top: #8db6e6;
    --cream: #f7ecca;
    --nav-active: #7fabe0;
    --nav-text: #ffffff;
    --nav-active-text: #55677a;
    --headline: #6e6a5e;
    --pill: #4f8fd8;
    --dot: #7fb0de;
    --card-about: #3d8be2;
    --card-products: #1c5ead;
    --card-services: #3f77b7;
    --card-customers: #1f4d84;
    --ink: #222222;
    --rule: #4d79a6;
    --link-blue: #2a68b8;
    --quote-mark: #e4dcbc;
    --photo-top: #27356e;
    --photo-bottom: #16263d;
    --thumb-top: #2f6a3a;
    --thumb-bottom: #1d4426;
  }
  * { box-sizing: border-box; margin: 0; padding: 0; }
  html, body { width: 1200px; height: 975px; overflow: hidden; }
  body {
    background: var(--page-blue);
    font-family: "Questrial", "Century Gothic", sans-serif;
    color: var(--ink);
  }
  .page {
    position: relative;
    width: 1108px;
    height: 900px;
    transform: scale(1.0830);
    transform-origin: 0 0;
    background: linear-gradient(var(--page-blue-top) 0 4px, var(--page-blue) 4px);
  }
  .abs { position: absolute; }

  /* header */
  .brand {
    left: 211px; top: 20px; width: 125px;
    color: #2f5fa8; text-align: center; line-height: 1;
  }
  .brand-mark { font-size: 30px; letter-spacing: 3px; }
  .brand-name { font-size: 11px; letter-spacing: 1px; margin-top: 2px; }
  .main-nav { left: 0; top: 5px; width: 1108px; height: 56px; }
  .main-nav a {
    position: absolute; top: 0; height: 56px;
    padding-top: 33px; line-height: 16px;
    color: var(--nav-text); text-decoration: none; font-size: 12.5px; white-space: nowrap;
  }
  .main-nav a.active {
    background: var(--nav-active); color: var(--nav-active-text);
    width: 81px; text-align: center;
  }

  /* hero */
  .hero { left: 211px; top: 73px; width: 683px; height: 332px; background: var(--cream); }
  .hero-photo {
    left: 0; top: 0; width: 461px; height: 332px;
    background: linear-gradient(180deg, var(--photo-top), var(--photo-bottom));
  }
  .hero-title {
    left: 486px; top: 95px; width: 190px; font-weight: 400;
    font-size: 23px; line-height: 27px; letter-spacing: 1.6px; color: var(--headline);
  }
  .pill-button {
    left: 486px; top: 220px; width: 67px; height: 19px; border-radius: 10px;
    background: var(--pill); color: #fff; font-size: 9px; letter-spacing: 0.8px;
    text-align: center; line-height: 19px; font-weight: 700;
  }
  .slider-dots { left: 487px; top: 292px; display: flex; gap: 7px; }
  .slider-dots span { width: 10px; height: 10px; border-radius: 50%; background: var(--dot); }
  .slider-dots span.current { background: #fff; border: 1px solid var(--dot); }

  /* feature cards */
  .features { left: 211px; top: 408px; width: 683px; height: 164px; display: flex; }
  .feature { position: relative; height: 164px; color: #fff; padding: 17px 0 0 16px; }
  .feature h2 { font-weight: 400; font-size: 23px; line-height: 26px; margin-bottom: 11px; }
  .feature p { font-size: 7.8px; line-height: 9.4px; width: 140px; padding-left: 4px; }
  .feature .more { font-size: 8px; position: absolute; top: 133px; }
  .feature-about { width: 170px; background: var(--card-about); }
  .feature-products { width: 171px; background: var(--card-products); }
  .feature-services { width: 171px; background: var(--card-services); }
  .feature-customers { width: 171px; background: var(--card-customers); padding-left: 14px; }

  /* lower panel */
  .lower { left: 211px; top: 577px; width: 683px; height: 246px; background: var(--cream); }
  .section-title { font-size: 17px; letter-spacing: 0.8px; color: #333; font-weight: 400; }
  .principles-title { left: 19px; top: 26px; }
  .principles-text { left: 15px; top: 61px; width: 142px; font-size: 7.8px; line-height: 9.4px; }
  .principles-text p + p { margin-top: 9px; }
  .news-title { left: 191px; top: 26px; }
  .news-item { left: 186px; width: 154px; }
  .news-thumb {
    position: absolute; left: 0; top: 0; width: 44px; height: 32px;
    background: linear-gradient(180deg, var(--thumb-top), var(--thumb-bottom));
  }
  .news-text { position: absolute; left: 50px; top: 0; width: 100px; font-size: 7.8px; line-height: 9.4px; }
  .news-date { position: absolute; left: 3px; font-size: 8px; }
  .news-one { top: 59px; height: 59px; border-bottom: 1px solid var(--rule); width: 153px; }
  .news-one .news-date { top: 45px; }
  .news-two { top: 136px; }
  .news-two .news-date { top: 41px; }

  .testimonial { left: 360px; top: 20px; width: 315px; height: 100px; }
  .quote-mark { position: absolute; left: 0; top: 0; }
  .quote-text {
    position: absolute; left: 59px; top: 17px; width: 220px;
    font-family: "Arimo", Arial, sans-serif; font-weight: 700; font-size: 7.3px; line-height: 9.5px; color: #333;
  }
  .quote-author { position: absolute; left: 56px; top: 59px; font-size: 8px; letter-spacing: 0.6px; color: #333; }
  .more-testimonials { position: absolute; left: 190px; top: 80px; font-size: 8px; color: var(--link-blue); letter-spacing: 0.4px; }
  .testimonial-rule { left: 363px; top: 122px; width: 311px; border-top: 1px solid var(--rule); }
  .client-row { left: 363px; top: 138px; width: 315px; height: 50px; }
  .client-logo {
    position: absolute; top: 2px; width: 67px; height: 47px; background: #fff; border: 1px solid #cfcfcf;
    display: flex; align-items: center; justify-content: center; gap: 3px;
    font-size: 10px; color: #1e3f7a;
  }
  .client-logo i { width: 7px; height: 7px; border-radius: 50%; background: #1e3f7a; display: block; }
  .arrow { position: absolute; top: 10px; }

  /* footer */
  .social { left: 211px; top: 843px; display: flex; gap: 14px; font-size: 8.5px; color: #fff; }
  .social span { display: flex; align-items: center; gap: 6px; }
  .social i { display: block; width: 11px; height: 11px; background: #dce9f7; }
  .copyright { left: 211px; top: 860px; font-size: 8px; color: #fff; }
  .contact-lines { right: 215px; top: 843px; font-size: 8px; color: #fff; text-align: right; line-height: 15px; }
</style>
</head>
<body>
<div class="page">
  <header>
    <div class="abs brand" aria-label="RVD Worldwide Limited">
      <div class="brand-mark">RVD</div>
      <div class="brand-name">Worldwide Limited</div>
    </div>
    <nav class="abs main-nav">
      <a class="active" href="#" style="left:397px">Home</a>
      <a href="#" style="left:497px">About Us</a>
      <a href="#" style="left:584px">Products</a>
      <a href="#" style="left:670px">Services</a>
      <a href="#" style="left:752px">Clients</a>
      <a href="#" style="left:823px">Contacts</a>
    </nav>
  </header>

  <section class="abs hero">
    <div class="abs hero-photo" role="img" aria-label="Photo of a hand probing a printed circuit board"></div>
    <h1 class="abs hero-title">Give your Business the Technology Edge</h1>
    <div class="abs pill-button">Read More</div>
    <div class="abs slider-dots"><span></span><span class="current"></span><span></span><span></span><span></span></div>
  </section>

  <section class="abs features">
    <div class="feature feature-about">
      <h2>About Us</h2>
      <p>We approach each customer with a long-term partnership view that delivers the lowest ownership costs and highest total values to our customers. We customize quotations and solutions in order to allow our customers to win more businesses.</p>
      <span class="more">Read More &gt;</span>
    </div>
    <div class="feature feature-products">
      <h2>Products</h2>
      <p>We approach each customer with a long-term partnership view that delivers the lowest ownership costs and highest total values to our customers. We customize quotations and solutions in order to allow our customers to win more businesses.</p>
      <span class="more">Read More &gt;</span>
    </div>
    <div class="feature feature-services">
      <h2>Services</h2>
      <p>We approach each customer with a long-term partnership view that delivers the lowest ownership costs and highest total values to our customers. We customize quotations and solutions in order to allow our customers to win more businesses.</p>
      <span class="more">Read More &gt;</span>
    </div>
    <div class="feature feature-customers">
      <h2>Customers</h2>
      <p>We approach each customer with a long-term partnership view that delivers the lowest ownership costs and highest total values to our customers. We customize quotations and solutions in order to allow our customers to win more businesses.</p>
      <span class="more">Read More &gt;</span>
    </div>
  </section>

  <section class="abs lower">
    <h3 class="abs section-title principles-title">Principles</h3>
    <div class="abs principles-text">
      <p>We approach each customer with a long-term partnership view that delivers the lowest ownership costs and highest total values to our customers.</p>
      <p>We customize quotations and solutions in order to allow our customers to win more businesses. We believe by thinking from our customers' points of view we will be able to create a WIN-WIN relationship.</p>
    </div>

    <h3 class="abs section-title news-title">News</h3>
    <div class="abs news-item news-one">
      <div class="news-thumb" role="img" aria-label="Circuit board thumbnail photo"></div>
      <div class="news-text">RVD could warehouse products in order to ensure just in time delivery.</div>
      <div class="news-date">December 16, 2011</div>
    </div>
    <div class="abs news-item news-two">
      <div class="news-thumb" role="img" aria-label="Circuit board thumbnail photo"></div>
      <div class="news-text">RVD could warehouse products in order to ensure just in time delivery.</div>
      <div class="news-date">February 27, 2012</div>
    </div>

    <div class="abs testimonial">
      <svg class="quote-mark" width="52" height="50" viewBox="0 0 52 50" aria-hidden="true">
        <path d="M2 2h22v26c0 10-6 18-16 20l-2-6c5-2 8-6 8-12H2z M28 2h22v26c0 10-6 18-16 20l-2-6c5-2 8-6 8-12H28z" fill="var(--quote-mark)"/>
      </svg>
      <p class="quote-text">Neque porro quisquam est qui dolorem ipsum quia dolor sit amet, consectetur, adipisci velit...Neque porro quisquam est qui dolorem ipsum quia dolor sit amet, consectetur, adipisci velit...</p>
      <p class="quote-author">- Daniel Harlow, Norvane</p>
      <a class="more-testimonials">More Testimonials</a>
    </div>
    <div class="abs testimonial-rule"></div>
    <div class="abs client-row">
      <svg class="arrow" style="left:0" width="20" height="30" viewBox="0 0 20 30" aria-hidden="true"><path d="M16 2 4 15l12 13" fill="none" stroke="#dfe8f2" stroke-width="3"/></svg>
      <div class="client-logo" style="left:32px"><i></i>Norvane</div>
      <div class="client-logo" style="left:117px">Kelmira</div>
      <div class="client-logo" style="left:200px"><i></i>Toravex</div>
      <svg class="arrow" style="left:278px" width="20" height="30" viewBox="0 0 20 30" aria-hidden="true"><path d="M4 2l12 13L4 28" fill="none" stroke="#dfe8f2" stroke-width="3"/></svg>
    </div>
  </section>

  <footer>
    <div class="abs social">
      <span><i></i>Chirpline</span>
      <span><i></i>Friendsquare</span>
      <span><i></i>Circlehub</span>
    </div>
    <div class="abs copyright">RVD Worldwide © Copyright 2012</div>
    <div class="abs contact-lines">Telephone: (852)35550142<br>Fax: (852)35550187</div>
  </footer>
</div>
</body>
</html>
```